Pluva

We need ideas for powerpoint template. Please submit several designs from simple/basic to elaborate/detailed using our company's logo. Please match designs with our logo color. We're very open to ideas. "Harbors Harmonized" can be removed

```html
<!DOCTYPE html>
<html lang="en">
<head>
<meta charset="utf-8">
<title>Pluva – Presentation Template Overview</title>
<link href="https://fonts.googleapis.com/css2?family=Open+Sans:wght@400;600;700;800&display=swap" rel="stylesheet">
<style>
:root{
  --teal:#2f8c92;
  --teal-d:#1c6670;
  --teal-l:#6cbcbc;
  --teal-xl:#e1f1f1;
  --yel:#f6c20f;
  --slate:#4d5877;
  --ink:#3e4a4f;
  --mute:#8c9295;
  --panel:#f1f3f3;
  --bg:#e9e9e9;
  --white:#ffffff;
}
*{box-sizing:border-box;margin:0;padding:0}
html,body{width:707px;height:1200px;overflow:hidden}
body{background:var(--bg);font-family:'Open Sans',sans-serif;color:var(--ink)}
.deck{position:relative;width:707px;height:1200px}
.grid{position:absolute;left:6px;top:6px;display:grid;grid-template-columns:repeat(3,229px);grid-auto-rows:129px;gap:3.3px 4.5px}
.grid-last{position:absolute;left:132px;top:1064px;display:flex;gap:6px}
.slide{position:relative;width:229px;height:129px;background:var(--white);overflow:hidden}
.abs{position:absolute}
.hdr{position:absolute;left:0;top:0;width:100%;height:14px;background:linear-gradient(90deg,var(--teal-d),var(--teal))}
.hdr::after{content:"";position:absolute;right:0;top:0;width:70px;height:14px;background:var(--teal-l);opacity:.55;clip-path:polygon(22% 0,100% 0,100% 100%,0 100%)}
.hdr span{position:relative;z-index:1;display:block;font-size:8.2px;font-weight:600;color:var(--white);line-height:14px;padding-left:6px}
.foot{position:absolute;left:0;right:0;bottom:0;height:10px}
.foot::before{content:"";position:absolute;left:14px;right:14px;bottom:4px;height:.6px;background:var(--teal-l)}
.foot-mark{position:absolute;left:4px;bottom:2px;width:6px;height:6px;border-radius:50%;background:var(--teal)}
.pg{position:absolute;right:3px;bottom:2px;width:8px;height:5px;background:var(--teal);color:var(--white);font-size:3px;line-height:5px;text-align:center;font-style:normal}
.tx{font-size:3.5px;line-height:4.6px;color:var(--mute)}
.tx-w{font-size:3.5px;line-height:4.6px;color:var(--white)}
.tt{font-size:3.8px;font-weight:700;color:var(--ink);line-height:5px}
.tt-teal{font-size:3.8px;font-weight:700;color:var(--teal);line-height:5px}
.photo{position:absolute}
/* cover */
.cover-photo{left:0;top:0;width:229px;height:112px;background:radial-gradient(circle at 30% 30%,#5fb3c0 0,#1d5a70 45%,#0d2f45 100%);clip-path:polygon(0 0,100% 0,100% 58%,0 84%)}
.cover-band{left:0;top:0;width:229px;height:112px;background:var(--teal);opacity:.75;clip-path:polygon(0 84%,100% 58%,100% 66%,0 92%)}
.cover-title{left:0;right:0;top:39px;text-align:center;color:var(--white);font-weight:700;font-size:10.5px;letter-spacing:.1px}
.cover-mark{left:98px;top:72px;width:33px;height:33px;border-radius:50%;background:var(--teal);border:2px solid var(--white)}
.cover-name{left:0;right:0;top:106px;text-align:center;color:var(--teal);font-weight:700;font-size:7px}
/* deck name */
.name-photo{left:0;top:0;width:229px;height:104px;background:radial-gradient(circle at 70% 30%,#5aa9b0 0,#2f8c92 40%,#1c6670 100%)}
.name-title{left:0;right:0;top:46px;text-align:center;color:var(--white);font-size:11px;font-weight:400}
.name-sub{left:0;right:0;top:61px;text-align:center;color:var(--white);font-size:5px}
.mini-brand{left:6px;bottom:3px;display:flex;flex-direction:column;align-items:center;gap:1px}
.mini-brand i{width:13px;height:13px;border-radius:50%;background:var(--teal);display:block}
.mini-brand b{font-size:3.6px;color:var(--teal);font-weight:700}
/* lists */
.num-circ{width:9px;height:9px;border-radius:50%;border:1px solid var(--teal);font-size:3.6px;color:var(--teal);text-align:center;line-height:7px;font-weight:700}
.num{font-size:7px;font-weight:700;color:var(--ink)}
.vline{width:.6px;height:18px;background:var(--mute)}
.tick{width:6px;height:6px;border-radius:50%;background:var(--teal);position:relative}
.tick::after{content:"";position:absolute;left:1.7px;top:1.1px;width:1.5px;height:2.6px;border:solid var(--white);border-width:0 .7px .7px 0;transform:rotate(45deg)}
.chev{height:9px;background:var(--white);border:.6px solid #bfc8c9;font-size:3.6px;font-weight:700;color:var(--ink);text-align:center;line-height:8px;clip-path:polygon(0 0,88% 0,100% 50%,88% 100%,0 100%,10% 50%)}
.chev.on{background:var(--teal);color:var(--white);border-color:var(--teal)}
/* table */
.fin{position:absolute;left:18px;top:30px;width:195px;border-collapse:collapse;font-size:3.3px;color:var(--ink)}
.fin td,.fin th{padding:0 2px;height:4.4px;line-height:4.4px;text-align:left;white-space:nowrap}
.fin th{background:var(--teal);color:var(--white);font-weight:700}
.fin .hl td{background:var(--teal-l);color:var(--white)}
.fin .hl-y td{background:var(--yel);color:var(--white)}
.fin .gap td{height:3px}
.fin td.v{background:var(--panel)}
/* points */
.pts{position:absolute;top:38px;width:96px;height:76px;background:var(--panel)}
.pts-h{height:6px;font-size:3.2px;color:var(--white);text-align:center;line-height:6px;font-weight:700}
.pt{display:flex;gap:3px;padding:3px 5px 0}
.pt i{flex:none;width:5px;height:5px;border-radius:50%;border:.7px solid var(--teal)}
.pt.neg i{border-color:var(--yel)}
/* section */
.sec-band{left:96px;top:56px;width:133px;height:26px;background:var(--teal);padding:5px 0 0 8px}
.sec-band b{display:block;font-size:10px;color:var(--white);font-weight:400;line-height:11px}
.sec-band span{display:block;font-size:3.6px;color:var(--white)}
/* city */
.city{left:0;top:0;width:229px;height:129px;background:linear-gradient(180deg,#4c7b9e 0,#2a4f6f 55%,#1c3652 100%)}
.city-title{left:50px;top:44px;font-size:12px;font-weight:700;color:var(--white)}
.vrow{position:absolute;left:0;width:229px;height:10px;background:rgba(20,40,60,.72);display:flex;align-items:center;padding:0 6px;gap:10px}
.vrow.hot{background:var(--yel)}
.vrow b{margin-left:auto;color:var(--white);font-size:6.5px;font-weight:600}
.box{position:absolute}
.ttl-big{font-size:9px;font-weight:700;color:var(--teal)}
</style>
</head>
<body>
<main class="deck">
<section class="grid">

<!-- 1 cover -->
<article class="slide">
  <div class="photo cover-photo" role="img" aria-label="Dark teal network of glowing connected points"></div>
  <div class="abs cover-band"></div>
  <h1 class="abs cover-title">YOUR SLIDES DECK TITLE</h1>
  <div class="abs cover-mark"></div>
  <div class="abs cover-name">Pluva</div>
</article>

<!-- 2 deck name -->
<article class="slide">
  <div class="photo name-photo" role="img" aria-label="Soft teal network texture"></div>
  <h2 class="abs name-title">Your Slides Deck Name</h2>
  <p class="abs name-sub">Your Slides Deck Name</p>
  <div class="abs mini-brand"><i></i><b>Pluva</b></div>
  <div class="foot"><i class="pg">2</i></div>
</article>

<!-- 3 about -->
<article class="slide">
  <div class="hdr"><span>About Us</span></div>
  <p class="abs tx" style="left:10px;top:20px;width:122px">Our team plans clear events for every client, from the first call to the last guest. We listen, shape the plan, and keep each step simple. <b style="color:var(--ink)">Every detail is checked twice</b> so the day runs on time and on budget for all.</p>
  <p class="abs tx" style="left:10px;top:52px;width:122px">We work with venues, speakers and crews across many cities. Each project has one lead who stays with you the whole way. <b style="color:var(--ink)">One lead, one plan, one team</b> that knows your goals and delivers them well.</p>
  <div class="abs" style="left:144px;top:18px;display:grid;gap:4px">
    <div style="display:flex;gap:4px"><div class="num-circ">01</div><div><div class="tt-teal" style="font-size:3px">Your Text Here</div><div class="tx" style="width:68px">Short note on this point goes here.</div></div></div>
    <div style="display:flex;gap:4px"><div class="num-circ">02</div><div><div class="tt-teal" style="font-size:3px">Your Text Here</div><div class="tx" style="width:68px">Short note on this point goes here.</div></div></div>
    <div style="display:flex;gap:4px"><div class="num-circ">03</div><div><div class="tt-teal" style="font-size:3px">Your Text Here</div><div class="tx" style="width:68px">Short note on this point goes here.</div></div></div>
    <div style="display:flex;gap:4px"><div class="num-circ">04</div><div><div class="tt-teal" style="font-size:3px">Your Text Here</div><div class="tx" style="width:68px">Short note on this point goes here.</div></div></div>
  </div>
  <div class="foot"><i class="foot-mark"></i><i class="pg">3</i></div>
</article>

<!-- 4 numbered -->
<article class="slide">
  <div class="hdr"><span>Lorem ipsum dolor</span></div>
  <div class="abs" style="left:4px;top:24px;display:grid;grid-template-columns:repeat(4,55px);row-gap:12px">
    <div style="display:flex;gap:2px;align-items:flex-start"><span class="num">01</span><i class="vline"></i><div><div class="tt" style="font-size:3px">Lorem ipsum dolor</div><div class="tx" style="font-size:3px;line-height:3.8px">Plan the brief and set the goals.</div></div></div>
    <div style="display:flex;gap:2px;align-items:flex-start"><span class="num">02</span><i class="vline"></i><div><div class="tt" style="font-size:3px">Lorem ipsum dolor</div><div class="tx" style="font-size:3px;line-height:3.8px">Book the venue and the dates.</div></div></div>
    <div style="display:flex;gap:2px;align-items:flex-start"><span class="num">03</span><i class="vline"></i><div><div class="tt" style="font-size:3px">Lorem ipsum dolor</div><div class="tx" style="font-size:3px;line-height:3.8px">Invite speakers and confirm them.</div></div></div>
    <div style="display:flex;gap:2px;align-items:flex-start"><span class="num">04</span><i class="vline"></i><div><div class="tt" style="font-size:3px">Lorem ipsum dolor</div><div class="tx" style="font-size:3px;line-height:3.8px">Open sign up for every guest.</div></div></div>
    <div style="display:flex;gap:2px;align-items:flex-start"><span class="num">05</span><i class="vline"></i><div><div class="tt" style="font-size:3px">Lorem ipsum dolor</div><div class="tx" style="font-size:3px;line-height:3.8px">Set travel and rooms for all.</div></div></div>
    <div style="display:flex;gap:2px;align-items:flex-start"><span class="num">06</span><i class="vline"></i><div><div class="tt" style="font-size:3px">Lorem ipsum dolor</div><div class="tx" style="font-size:3px;line-height:3.8px">Print badges and the program.</div></div></div>
    <div style="display:flex;gap:2px;align-items:flex-start"><span class="num">07</span><i class="vline"></i><div><div class="tt" style="font-size:3px">Lorem ipsum dolor</div><div class="tx" style="font-size:3px;line-height:3.8px">Run the day with one lead.</div></div></div>
    <div style="display:flex;gap:2px;align-items:flex-start"><span class="num">08</span><i class="vline"></i><div><div class="tt" style="font-size:3px">Lorem ipsum dolor</div><div class="tx" style="font-size:3px;line-height:3.8px">Share notes and a full report.</div></div></div>
  </div>
  <div class="abs" style="left:0;top:94px;width:229px;height:27px;background:linear-gradient(90deg,var(--teal-l),var(--teal));padding-top:7px;text-align:center;font-size:4.6px;color:var(--white);font-weight:600;line-height:6px">Lorem ipsum dolor sit amet, consectetur adipiscing elit,<br>sed do eiusmod tempor</div>
  <div class="foot"><i class="pg">4</i></div>
</article>

<!-- 5 services -->
<article class="slide">
  <div class="hdr"><span>Our Services</span></div>
  <div class="abs" style="left:26px;top:24px;display:grid;grid-template-columns:102px 80px;row-gap:6px">
    <div style="display:flex;gap:4px"><i class="tick"></i><div><div class="tt" style="font-size:3.2px">Lorem ipsum dolor</div><div class="tx" style="width:64px;font-size:3px;line-height:3.9px">Full event plans built for each brief and run by one steady team.</div></div></div>
    <div style="display:flex;gap:4px"><i class="tick"></i><div><div class="tt" style="font-size:3.2px">Lorem ipsum dolor</div><div class="tx" style="width:64px;font-size:3px;line-height:3.9px">Venue search with clear costs and a short list to choose from.</div></div></div>
    <div style="display:flex;gap:4px"><i class="tick"></i><div><div class="tt" style="font-size:3.2px">Lorem ipsum dolor</div><div class="tx" style="width:64px;font-size:3px;line-height:3.9px">Speaker care from the first invite to the final thank you note.</div></div></div>
    <div style="display:flex;gap:4px"><i class="tick"></i><div><div class="tt" style="font-size:3.2px">Lorem ipsum dolor</div><div class="tx" style="width:64px;font-size:3px;line-height:3.9px">Guest sign up, badges and help desk on the day itself.</div></div></div>
    <div style="display:flex;gap:4px"><i class="tick"></i><div><div class="tt" style="font-size:3.2px">Lorem ipsum dolor</div><div class="tx" style="width:64px;font-size:3px;line-height:3.9px">Travel and rooms for guests with one point of contact.</div></div></div>
    <div style="display:flex;gap:4px"><i class="tick"></i><div><div class="tt" style="font-size:3.2px">Lorem ipsum dolor</div><div class="tx" style="width:64px;font-size:3px;line-height:3.9px">Reports after the event with notes for the next one.</div></div></div>
  </div>
  <div class="foot"><i class="foot-mark"></i><i class="pg">5</i></div>
</article>

<!-- 6 steps -->
<article class="slide">
  <div class="hdr"><span>Lorem ipsum dolor</span></div>
  <svg class="abs" style="left:0;top:40px" width="229" height="16" viewBox="0 0 229 16">
    <g fill="var(--ink)">
      <circle cx="42" cy="8" r="5"/><circle cx="42" cy="8" r="2" fill="#fff"/>
      <ellipse cx="90" cy="8" rx="7" ry="2.6" fill="none" stroke="var(--ink)" stroke-width="1"/><ellipse cx="90" cy="8" rx="2.6" ry="7" fill="none" stroke="var(--ink)" stroke-width="1"/>
      <path d="M137 2h5v4l4 8h-13l4-8z"/>
      <path d="M183 14l3-5 6-6 3 3-6 6z"/>
    </g>
  </svg>
  <div class="abs" style="left:20px;top:60px;display:flex;gap:2px">
    <div class="chev" style="width:46px">Contents Title</div>
    <div class="chev" style="width:46px">Contents Title</div>
    <div class="chev on" style="width:46px">Contents Title</div>
    <div class="chev" style="width:46px">Contents Title</div>
  </div>
  <div class="abs" style="left:22px;top:73px;display:grid;grid-template-columns:repeat(4,48px);text-align:center">
    <p class="tx" style="font-size:3px;line-height:3.9px">Short note for this step of the plan here.</p>
    <p class="tx" style="font-size:3px;line-height:3.9px">Short note for this step of the plan here.</p>
    <p class="tx" style="font-size:3px;line-height:3.9px">Short note for this step of the plan here.</p>
    <p class="tx" style="font-size:3px;line-height:3.9px">Short note for this step of the plan here.</p>
  </div>
  <div class="foot"><i class="foot-mark"></i><i class="pg">6</i></div>
</article>

<!-- 7 icon intro -->
<article class="slide">
  <div class="photo" style="left:0;top:0;width:229px;height:70px;background:linear-gradient(120deg,#2a7d86,#3a9aa0 60%,#2f8c92)" role="img" aria-label="Soft teal office backdrop"></div>
  <h2 class="abs" style="left:0;right:0;top:22px;text-align:center;color:var(--white);font-size:10px;font-weight:600">Lorem ipsum dolor</h2>
  <p class="abs" style="left:0;right:0;top:35px;text-align:center;color:var(--white);font-size:3.6px">Lorem ipsum dolor sit amet, consectetur adipiscing elit</p>
  <svg class="abs" style="left:0;top:58px" width="229" height="22" viewBox="0 0 229 22">
    <g fill="#fff" stroke="var(--teal-l)" stroke-width="1"><circle cx="50" cy="11" r="10"/><circle cx="115" cy="11" r="10"/><circle cx="180" cy="11" r="10"/></g>
    <g fill="var(--ink)"><path d="M46 6h8v3a4 4 0 0 1-8 0zM49 13h2v3h3v1h-8v-1h3z"/><circle cx="114" cy="10" r="3" fill="none" stroke="var(--ink)" stroke-width="1.2"/><path d="M116 12l3 3" stroke="var(--ink)" stroke-width="1.4"/><circle cx="180" cy="10" r="3.4" fill="var(--yel)"/><rect x="178.5" y="14" width="3" height="2"/></g>
  </svg>
  <div class="abs" style="left:0;top:83px;width:229px;display:grid;grid-template-columns:repeat(3,1fr);text-align:center;padding:0 22px;gap:10px">
    <div><div class="tt-teal" style="font-size:3.6px">Lorem ipsum dolor</div><p class="tx" style="font-size:3px;line-height:3.9px">Short note that explains this point in a few plain words.</p></div>
    <div><div class="tt-teal" style="font-size:3.6px">Lorem ipsum dolor</div><p class="tx" style="font-size:3px;line-height:3.9px">Short note that explains this point in a few plain words.</p></div>
    <div><div class="tt-teal" style="font-size:3.6px">Lorem ipsum dolor</div><p class="tx" style="font-size:3px;line-height:3.9px">Short note that explains this point in a few plain words.</p></div>
  </div>
  <div class="foot"><i class="foot-mark"></i><i class="pg">7</i></div>
</article>

<!-- 8 table -->
<article class="slide">
  <div class="hdr"><span>Lorem ipsum dolor</span></div>
  <p class="abs" style="left:0;right:0;top:22px;text-align:center;font-size:3.4px;color:var(--teal)">Lorem ipsum dolor sit amet, consectetur adipiscing elit</p>
  <table class="fin">
    <tr><td></td><td></td><th>2019</th><th>2020</th><th>2021</th><th>2022</th></tr>
    <tr><td><b>Revenue</b></td><td></td><td></td><td></td><td></td><td></td></tr>
    <tr><td>Licence fees</td><td>£</td><td class="v">1,787,100</td><td class="v">6,177,000</td><td class="v">10,807,000</td><td class="v">28,194,000</td></tr>
    <tr><td>Revenue share</td><td>£</td><td class="v">630,000</td><td class="v">11,474,750</td><td class="v">15,414,000</td><td class="v">13,414,000</td></tr>
    <tr><td>Development Fee Revenue</td><td>£</td><td class="v">100,000</td><td class="v">200,000</td><td class="v">200,000</td><td class="v">200,000</td></tr>
    <tr class="hl"><td>Total Revenue</td><td>£</td><td>2,517,100</td><td>17,851,750</td><td>28,421,000</td><td>28,194,000</td></tr>
    <tr class="gap"><td colspan="6"></td></tr>
    <tr class="hl"><td>Operating costs</td><td>£</td><td>1,408,910</td><td>2,522,838</td><td>2,852,815</td><td>2,979,113</td></tr>
    <tr class="gap"><td colspan="6"></td></tr>
    <tr class="hl"><td>OPERATING PROFIT</td><td>£</td><td>1,108,190</td><td>15,328,912</td><td>25,568,185</td><td>25,214,887</td></tr>
    <tr class="gap"><td colspan="6"></td></tr>
    <tr class="hl-y"><td>NET PROFIT</td><td>£</td><td>897,634</td><td>12,569,708</td><td>19,325,895</td><td>20,928,356</td></tr>
  </table>
  <div class="foot"><i class="foot-mark"></i><i class="pg">8</i></div>
</article>

<!-- 9 points -->
<article class="slide">
  <div class="hdr"><span>Lorem ipsum dolor</span></div>
  <svg class="abs" style="left:28px;top:20px" width="12" height="12" viewBox="0 0 12 12"><circle cx="6" cy="6" r="5" fill="none" stroke="var(--teal)" stroke-width="1"/><path d="M3.5 6l2 2 3-4" fill="none" stroke="var(--teal)" stroke-width="1"/></svg>
  <svg class="abs" style="left:143px;top:20px" width="12" height="12" viewBox="0 0 12 12"><circle cx="6" cy="6" r="5" fill="none" stroke="var(--yel)" stroke-width="1"/><path d="M4 4l4 4M8 4l-4 4" stroke="var(--yel)" stroke-width="1"/></svg>
  <div class="pts" style="left:26px">
    <div class="pts-h" style="background:var(--teal)">POSITIVE POINTS</div>
    <div class="pt"><i></i><div><div class="tt-teal" style="font-size:3px;line-height:3.6px">TITLE GOES HERE</div><div class="tx" style="font-size:2.8px;line-height:3.4px">Short note on the good side of this plan.</div></div></div>
    <div class="pt"><i></i><div><div class="tt-teal" style="font-size:3px;line-height:3.6px">TITLE GOES HERE</div><div class="tx" style="font-size:2.8px;line-height:3.4px">Short note on the good side of this plan.</div></div></div>
    <div class="pt"><i></i><div><div class="tt-teal" style="font-size:3px;line-height:3.6px">TITLE GOES HERE</div><div class="tx" style="font-size:2.8px;line-height:3.4px">Short note on the good side of this plan.</div></div></div>
    <div class="pt"><i></i><div><div class="tt-teal" style="font-size:3px;line-height:3.6px">TITLE GOES HERE</div><div class="tx" style="font-size:2.8px;line-height:3.4px">Short note on the good side of this plan.</div></div></div>
  </div>
  <div class="pts" style="left:116px">
    <div class="pts-h" style="background:var(--yel)">NEGATIVE POINTS</div>
    <div class="pt neg"><i></i><div><div class="tt" style="font-size:3px;line-height:3.6px;color:var(--yel)">TITLE GOES HERE</div><div class="tx" style="font-size:2.8px;line-height:3.4px">Short note on the risk side of this plan.</div></div></div>
    <div class="pt neg"><i></i><div><div class="tt" style="font-size:3px;line-height:3.6px;color:var(--yel)">TITLE GOES HERE</div><div class="tx" style="font-size:2.8px;line-height:3.4px">Short note on the risk side of this plan.</div></div></div>
    <div class="pt neg"><i></i><div><div class="tt" style="font-size:3px;line-height:3.6px;color:var(--yel)">TITLE GOES HERE</div><div class="tx" style="font-size:2.8px;line-height:3.4px">Short note on the risk side of this plan.</div></div></div>
    <div class="pt neg"><i></i><div><div class="tt" style="font-size:3px;line-height:3.6px;color:var(--yel)">TITLE GOES HERE</div><div class="tx" style="font-size:2.8px;line-height:3.4px">Short note on the risk side of this plan.</div></div></div>
  </div>
  <div class="foot"><i class="foot-mark"></i><i class="pg">9</i></div>
</article>

<!-- 10 org chart -->
<article class="slide">
  <div class="hdr"><span>Lorem ipsum dolor</span></div>
  <svg class="abs" style="left:0;top:14px" width="229" height="105" viewBox="0 0 229 105" font-family="Open Sans, sans-serif" font-size="3" text-anchor="middle">
    <g stroke="#c8cdcf" stroke-width=".6" fill="none">
      <path d="M114 18v6M40 24h148M40 24v4M114 24v4M188 24v4"/>
      <path d="M22 38v54M96 38v54M170 38v54"/>
      <path d="M22 48h6M22 70h6M22 92h6M96 48h6M96 70h6M96 92h6M170 48h6M170 70h6M170 92h6"/>
    </g>
    <rect x="94" y="8" width="40" height="5" fill="var(--teal)"/><rect x="94" y="13" width="40" height="5" fill="var(--teal-l)"/>
    <text x="114" y="12" fill="#fff">FIRST / LAST NAME</text><text x="114" y="17" fill="#fff" font-size="2.4">Position</text>
    <g>
      <rect x="18" y="28" width="44" height="5" fill="var(--yel)"/><rect x="18" y="33" width="44" height="5" fill="#f9d75a"/>
      <rect x="92" y="28" width="44" height="5" fill="var(--yel)"/><rect x="92" y="33" width="44" height="5" fill="#f9d75a"/>
      <rect x="166" y="28" width="44" height="5" fill="var(--yel)"/><rect x="166" y="33" width="44" height="5" fill="#f9d75a"/>
    </g>
    <g fill="#fff"><text x="40" y="32">FIRST / LAST NAME</text><text x="114" y="32">FIRST / LAST NAME</text><text x="188" y="32">FIRST / LAST NAME</text>
      <text x="40" y="37" font-size="2.4">Position</text><text x="114" y="37" font-size="2.4">Position</text><text x="188" y="37" font-size="2.4">Position</text></g>
    <g fill="#eef0f0" stroke="#d5d9da" stroke-width=".4">
      <rect x="28" y="44" width="38" height="9"/><rect x="28" y="66" width="38" height="9"/><rect x="28" y="88" width="38" height="9"/>
      <rect x="102" y="44" width="38" height="9"/><rect x="102" y="66" width="38" height="9"/><rect x="102" y="88" width="38" height="9"/>
      <rect x="176" y="44" width="38" height="9"/><rect x="176" y="66" width="38" height="9"/><rect x="176" y="88" width="38" height="9"/>
    </g>
    <g fill="#8c9295" font-size="2.4">
      <text x="47" y="48">FIRST / LAST NAME</text><text x="47" y="52">Position</text><text x="47" y="70">FIRST / LAST NAME</text><text x="47" y="74">Position</text><text x="47" y="92">FIRST / LAST NAME</text><text x="47" y="96">Position</text>
      <text x="121" y="48">FIRST / LAST NAME</text><text x="121" y="52">Position</text><text x="121" y="70">FIRST / LAST NAME</text><text x="121" y="74">Position</text><text x="121" y="92">FIRST / LAST NAME</text><text x="121" y="96">Position</text>
      <text x="195" y="48">FIRST / LAST NAME</text><text x="195" y="52">Position</text><text x="195" y="70">FIRST / LAST NAME</text><text x="195" y="74">Position</text><text x="195" y="92">FIRST / LAST NAME</text><text x="195" y="96">Position</text>
    </g>
  </svg>
  <div class="foot"><i class="foot-mark"></i><i class="pg">10</i></div>
</article>

<!-- 11 worldmap -->
<article class="slide">
  <div class="hdr"><span>Lorem ipsum dolor</span></div>
  <div class="photo" style="left:90px;top:16px;width:130px;height:60px;background:radial-gradient(ellipse at center,#dcebec 0,#ffffff 75%)" role="img" aria-label="Faint world map"></div>
  <p class="abs tx" style="left:36px;top:30px;width:160px;color:var(--ink)">We plan events in many cities and bring people together from every region. Each plan starts with your goals, your guests and your budget, and ends with a day that runs on time. <b>Clear steps, one team,</b> and reports you can share.</p>
  <div class="abs" style="left:0;top:78px;width:229px;height:42px;background:var(--teal)"></div>
  <div class="abs" style="left:16px;top:83px;color:var(--white);font-size:7.5px;font-weight:600;line-height:9px">Worldmap<br>Infographic</div>
  <p class="abs tx-w" style="left:16px;top:104px;width:86px;font-size:3px;line-height:3.9px">Short note on where our guests come from each year.</p>
  <svg class="abs" style="left:108px;top:80px" width="120" height="38" viewBox="0 0 120 38">
    <rect x="16" y="10" width="5" height="18" rx="2.5" fill="#fff"/>
    <circle cx="40" cy="19" r="10" fill="none" stroke="#ffffff55" stroke-width="4"/>
    <circle cx="40" cy="19" r="10" fill="none" stroke="var(--yel)" stroke-width="4" stroke-dasharray="37.7 62.8" transform="rotate(-90 40 19)"/>
    <text x="40" y="20.5" font-size="4" fill="#fff" text-anchor="middle" font-family="Open Sans, sans-serif" font-weight="700">60%</text>
    <circle cx="76" cy="19" r="10" fill="none" stroke="#ffffff55" stroke-width="4"/>
    <circle cx="76" cy="19" r="10" fill="none" stroke="var(--teal-xl)" stroke-width="4" stroke-dasharray="25.1 62.8" transform="rotate(-90 76 19)"/>
    <text x="76" y="20.5" font-size="4" fill="#fff" text-anchor="middle" font-family="Open Sans, sans-serif" font-weight="700">40%</text>
    <rect x="96" y="10" width="5" height="18" rx="2.5" fill="#fff"/>
  </svg>
  <div class="foot"><i class="foot-mark"></i><i class="pg">11</i></div>
</article>

<!-- 12 city -->
<article class="slide">
  <div class="photo city" role="img" aria-label="City skyline with tall glass towers"></div>
  <h2 class="abs city-title">Title Goes Here</h2>
  <div class="vrow" style="top:79px"><span class="tx-w" style="font-size:2.6px;line-height:3px;width:46px">Short note for this first value line</span><span class="tx-w" style="font-size:2.6px">Your Text Here</span><b>$ 64,090</b></div>
  <div class="vrow hot" style="top:92px"><span class="tx-w" style="font-size:2.6px;line-height:3px;width:46px">Short note for this second value line</span><span class="tx-w" style="font-size:2.6px">Your Text Here</span><b>$124,090</b></div>
  <div class="vrow" style="top:105px"><span class="tx-w" style="font-size:2.6px;line-height:3px;width:46px">Short note for this third value line</span><span class="tx-w" style="font-size:2.6px">Your Text Here</span><b>$234,090</b></div>
</article>

<!-- 13 petals + chart -->
<article class="slide">
  <div class="hdr"><span>Lorem ipsum dolor</span></div>
  <p class="abs tx" style="left:12px;top:19px;width:90px;font-size:2.8px;line-height:3.5px">Short note that opens this chart and tells the reader what to look for here.</p>
  <svg class="abs" style="left:30px;top:36px" width="64" height="66" viewBox="0 0 64 66" font-family="Open Sans, sans-serif" font-weight="700" font-size="5.5" fill="#fff" text-anchor="middle">
    <path d="M31 32V2A30 30 0 0 0 1 32z" fill="var(--slate)"/>
    <path d="M33 32V2A30 30 0 0 1 63 32z" fill="#5a6685"/>
    <path d="M31 34H1A30 30 0 0 0 31 64z" fill="#3dc6a7"/>
    <path d="M33 34h30A30 30 0 0 1 33 64z" fill="var(--teal-l)"/>
    <text x="18" y="24">60%</text><text x="46" y="24">90%</text><text x="18" y="50">80%</text><text x="46" y="50">70%</text>
  </svg>
  <svg class="abs" style="left:118px;top:20px" width="104" height="42" viewBox="0 0 104 42" font-family="Open Sans, sans-serif" font-size="2.4" fill="#8c9295">
    <path d="M10 2v34h92" stroke="#d0d4d5" stroke-width=".4" fill="none"/>
    <g><rect x="14" y="22" width="4" height="14" fill="var(--slate)"/><rect x="18" y="16" width="4" height="20" fill="var(--teal)"/><rect x="22" y="26" width="4" height="10" fill="#3dc6a7"/>
    <rect x="36" y="12" width="4" height="24" fill="var(--slate)"/><rect x="40" y="20" width="4" height="16" fill="var(--teal)"/><rect x="44" y="8" width="4" height="28" fill="#3dc6a7"/>
    <rect x="58" y="18" width="4" height="18" fill="var(--slate)"/><rect x="62" y="10" width="4" height="26" fill="var(--teal)"/><rect x="66" y="22" width="4" height="14" fill="#3dc6a7"/>
    <rect x="80" y="14" width="4" height="22" fill="var(--slate)"/><rect x="84" y="24" width="4" height="12" fill="var(--teal)"/><rect x="88" y="6" width="4" height="30" fill="#3dc6a7"/></g>
    <text x="14" y="40">Category 1</text><text x="36" y="40">Category 2</text><text x="58" y="40">Category 3</text><text x="80" y="40">Category 4</text>
  </svg>
  <div class="abs" style="left:126px;top:65px;display:grid;gap:3px">
    <div style="display:flex;gap:3px;align-items:center"><i style="width:4px;height:4px;border-radius:50%;background:var(--slate)"></i><span class="tx" style="font-size:2.6px;line-height:3.2px;width:80px">Short note for the first series in this chart.</span></div>
    <div style="display:flex;gap:3px;align-items:center"><i style="width:4px;height:4px;border-radius:50%;background:#5a6685"></i><span class="tx" style="font-size:2.6px;line-height:3.2px;width:80px">Short note for the second series in this chart.</span></div>
    <div style="display:flex;gap:3px;align-items:center"><i style="width:4px;height:4px;border-radius:50%;background:#3dc6a7"></i><span class="tx" style="font-size:2.6px;line-height:3.2px;width:80px">Short note for the third series in this chart.</span></div>
    <div style="display:flex;gap:3px;align-items:center"><i style="width:4px;height:4px;border-radius:50%;background:var(--teal-l)"></i><span class="tx" style="font-size:2.6px;line-height:3.2px;width:80px">Short note for the fourth series in this chart.</span></div>
  </div>
  <div class="foot"><i class="foot-mark"></i><i class="pg">13</i></div>
</article>

<!-- 14 section break -->
<article class="slide">
  <div class="abs sec-band"><b>Section Break</b><span>Insert the Sub Title of Your Presentation</span></div>
  <span class="abs" style="right:18px;bottom:4px;font-size:2.6px;color:var(--mute)">14</span>
</article>

<!-- 15 targets -->
<article class="slide">
  <div class="hdr"><span>Targets</span></div>
  <svg class="abs" style="left:8px;top:16px" width="100" height="108" viewBox="0 0 100 108" font-family="Open Sans, sans-serif">
    <path d="M58 10a38 38 0 0 1 36 30" fill="none" stroke="#a9b3b5" stroke-width="8"/>
    <path d="M94 44a38 38 0 0 1 -4 30" fill="none" stroke="#c3cacc" stroke-width="8"/>
    <path d="M88 78a38 38 0 0 1 -28 18" fill="none" stroke="#d8dddf" stroke-width="8"/>
    <circle cx="54" cy="50" r="22" fill="#fff" stroke="var(--teal)" stroke-width="4"/>
    <path d="M38 66l-24 24" stroke="var(--teal)" stroke-width="6" stroke-linecap="round"/>
    <text x="54" y="52" text-anchor="middle" font-size="7" font-weight="700" fill="var(--teal-d)">Targets</text>
    <text x="70" y="16" font-size="3.4" fill="#fff">01</text><text x="91" y="60" font-size="3.4" fill="#fff">02</text><text x="74" y="92" font-size="3.4" fill="#fff">03</text>
  </svg>
  <div class="abs" style="left:118px;top:26px;width:104px;display:grid;gap:6px">
    <div><div class="tt" style="font-size:3.8px">Target 01</div><p class="tx" style="font-size:3px;line-height:4px">Short note that explains the first target and the date we want to reach it.</p></div>
    <div><div class="tt" style="font-size:3.8px">Target 02</div><p class="tx" style="font-size:3px;line-height:4px">Short note that explains the second target and the date we want to reach it.</p></div>
    <div><div class="tt" style="font-size:3.8px">Target 03</div><p class="tx" style="font-size:3px;line-height:4px">Short note that explains the third target and the date we want to reach it.</p></div>
  </div>
  <div class="foot"><i class="foot-mark"></i><i class="pg">15</i></div>
</article>

<!-- 16 timeline -->
<article class="slide">
  <div class="hdr"><span>Timeline</span></div>
  <svg class="abs" style="left:0;top:60px" width="229" height="8" viewBox="0 0 229 8"><path d="M6 4h217" stroke="var(--teal)" stroke-width="1.2"/><g fill="var(--teal)"><circle cx="28" cy="4" r="1.8"/><circle cx="72" cy="4" r="1.8"/><circle cx="116" cy="4" r="1.8"/><circle cx="160" cy="4" r="1.8"/><circle cx="204" cy="4" r="1.8"/></g></svg>
  <div class="abs" style="left:22px;top:46px;font-size:4px;color:var(--teal-l);font-weight:700">2016</div>
  <div class="abs" style="left:105px;top:46px;font-size:4px;color:var(--teal-l);font-weight:700">2018</div>
  <div class="abs" style="left:194px;top:46px;font-size:4px;color:var(--teal-l);font-weight:700">2020</div>
  <div class="abs" style="left:66px;top:74px;font-size:4px;color:var(--teal-l);font-weight:700">2017</div>
  <div class="abs" style="left:154px;top:74px;font-size:4px;color:var(--teal-l);font-weight:700">2019</div>
  <p class="abs tx" style="left:52px;top:24px;width:40px;text-align:center;font-size:3px;line-height:3.9px;color:var(--ink)">First plan set and our first team of six joins.</p>
  <p class="abs tx" style="left:138px;top:24px;width:44px;text-align:center;font-size:3px;line-height:3.9px;color:var(--ink)">New office opens and we run ten events.</p>
  <p class="abs tx" style="left:8px;top:70px;width:38px;text-align:center;font-size:3px;line-height:3.9px;color:var(--ink)">First large meeting held for guests.</p>
  <p class="abs tx" style="left:94px;top:70px;width:44px;text-align:center;font-size:3px;line-height:3.9px;color:var(--ink)">Team grows and second city added.</p>
  <p class="abs tx" style="left:182px;top:70px;width:40px;text-align:center;font-size:3px;line-height:3.9px;color:var(--ink)">Events now run in twelve cities.</p>
  <div class="foot"><i class="foot-mark"></i><i class="pg">16</i></div>
</article>

<!-- 17 text + quote -->
<article class="slide">
  <div class="hdr" style="width:140px"><span>Lorem ipsum dolor sit</span></div>
  <div class="photo" style="left:150px;top:0;width:79px;height:62px;background:linear-gradient(135deg,#cfd6dc,#7d8b99 60%,#3c4a5a)" role="img" aria-label="Business people shaking hands over a laptop"></div>
  <p class="abs tx" style="left:12px;top:20px;width:126px;font-size:3px;line-height:3.9px">We keep each plan short and clear so every guest knows where to go and when. Our team checks each step and shares notes with you.</p>
  <div class="abs" style="left:10px;top:44px;width:118px;height:34px;background:var(--teal-l);padding:5px">
    <p class="tx-w" style="font-size:3px;line-height:3.9px">Short note in the box that shows the main idea of this page. Plans, guests and venues all in one place, with one lead who stays with you from start to end.</p>
  </div>
  <p class="abs tx" style="left:12px;top:86px;width:112px;font-size:3px;line-height:3.9px">We work with venues and crews in many cities, and we keep costs clear from the first call.</p>
  <div class="abs" style="left:130px;top:62px;width:99px;height:58px;background:var(--slate);padding:4px 10px;text-align:center">
    <div style="font-size:14px;color:#fff;line-height:12px;font-weight:700">&ldquo;</div>
    <p class="tx-w" style="font-size:3.2px;line-height:4.2px">Short quote from a happy client about the day and the team that ran it well.</p>
  </div>
  <div class="foot"><i class="foot-mark"></i><i class="pg">17</i></div>
</article>

<!-- 18 dna -->
<article class="slide">
  <div class="hdr"><span>Lorem ipsum dolor sit</span></div>
  <div class="photo" style="left:0;top:18px;width:229px;height:100px;background:linear-gradient(120deg,#3a9aa0,#246d78 50%,#6cbcbc)" role="img" aria-label="Teal science backdrop with a glowing helix"></div>
  <p class="abs tx-w" style="left:94px;top:24px;width:126px;font-size:3px;line-height:3.9px">Short note that sits over the image and tells the reader what this page is about and why it counts.</p>
  <p class="abs tx-w" style="left:94px;top:40px;width:126px;font-size:3px;line-height:3.9px">A second note adds a detail or two so the point is clear for everyone in the room.</p>
  <div class="abs" style="left:96px;top:62px;display:flex;gap:10px">
    <div style="display:flex;gap:3px"><i class="tick" style="background:#fff"></i><div><div class="tx-w" style="font-weight:700;font-size:3px">Lorem ipsum dolor</div><div class="tx-w" style="font-size:2.8px;line-height:3.5px;width:50px">Short note for this point.</div></div></div>
    <div style="display:flex;gap:3px"><i class="tick" style="background:#fff"></i><div><div class="tx-w" style="font-weight:700;font-size:3px">Lorem ipsum dolor</div><div class="tx-w" style="font-size:2.8px;line-height:3.5px;width:50px">Short note for this point.</div></div></div>
  </div>
  <div class="foot"><i class="foot-mark"></i><i class="pg">18</i></div>
</article>

<!-- 19 services package -->
<article class="slide">
  <div class="hdr"><span style="font-size:6.4px">Complete Services Package</span></div>
  <div class="abs" style="left:10px;top:20px;width:104px;display:grid;gap:5px">
    <p class="tx" style="font-size:3px;line-height:3.9px">Short note on the full package and what each client gets from the first call to the final report.</p>
    <p class="tx" style="font-size:3px;line-height:3.9px">Short note on planning, venues, guests and travel all handled by one team with one lead.</p>
    <p class="tx" style="font-size:3px;line-height:3.9px">Short note on the reports and follow up notes we share after each event ends.</p>
    <p class="tx" style="font-size:3px;line-height:3.9px">Short note on the price and how we keep every cost clear from day one.</p>
  </div>
  <div class="abs" style="left:122px;top:0;width:107px;height:129px;background:var(--teal)"></div>
  <p class="abs tx-w" style="left:140px;top:20px;width:80px;font-size:3px;font-weight:700">Lorem ipsum dolor sit amet, consectetur adipiscing</p>
  <div class="abs" style="left:136px;top:34px;display:grid;grid-template-columns:repeat(3,22px);gap:6px 8px">
    <div style="height:22px;background:#fff"></div><div style="height:22px;background:#fff"></div><div style="height:22px;background:#fff"></div>
    <div style="height:22px;background:#fff"></div><div style="height:22px;background:#fff"></div><div style="height:22px;background:#fff"></div>
  </div>
  <svg class="abs" style="left:136px;top:34px" width="82" height="50" viewBox="0 0 82 50" font-family="Open Sans, sans-serif" font-size="2.2" fill="var(--ink)" text-anchor="middle">
    <rect x="7" y="5" width="8" height="8" fill="none" stroke="var(--ink)" stroke-width=".8"/>
    <circle cx="41" cy="9" r="4" fill="none" stroke="var(--ink)" stroke-width=".8"/>
    <path d="M70 5l4 4-4 4-4-4z" fill="var(--ink)"/>
    <path d="M7 41l3-4 3 2 3-5" fill="none" stroke="var(--ink)" stroke-width=".8"/>
    <rect x="37" y="35" width="8" height="6" fill="var(--ink)"/>
    <circle cx="71" cy="38" r="3" fill="none" stroke="var(--ink)" stroke-width=".8"/>
    <text x="11" y="19">Event Planning</text><text x="41" y="19">Venue Search</text><text x="71" y="19">Speaker Care</text>
    <text x="11" y="47">Analytics</text><text x="41" y="47">Guest Desk</text><text x="71" y="47">What's next</text>
  </svg>
  <div class="foot"><i class="foot-mark"></i><i class="pg">19</i></div>
</article>

<!-- 20 problem -->
<article class="slide">
  <div class="abs" style="left:100px;top:0;width:129px;height:129px;background:var(--teal-xl);clip-path:polygon(30% 0,100% 0,80% 100%,0 100%)"></div>
  <svg class="abs" style="left:12px;top:10px" width="36" height="36" viewBox="0 0 36 36"><circle cx="18" cy="18" r="16" fill="none" stroke="var(--teal)" stroke-width="3"/><circle cx="18" cy="18" r="11" fill="#fff" stroke="var(--teal-l)" stroke-width=".8"/><text x="18" y="21" text-anchor="middle" font-family="Open Sans, sans-serif" font-size="9" fill="var(--teal-l)">?</text><circle cx="18" cy="34" r="2.5" fill="var(--teal-l)"/></svg>
  <h2 class="abs" style="left:66px;top:22px;font-size:9.5px;font-weight:700;color:var(--teal)">PROBLEM</h2>
  <p class="abs tx" style="left:66px;top:36px;width:148px;font-size:3px;line-height:3.9px;color:var(--ink)">Short note that sets out the problem our clients face when they plan an event alone, from venues and guests to costs that grow each week.</p>
  <div class="abs" style="left:78px;top:58px;display:grid;gap:4px;width:130px">
    <div style="display:flex;gap:3px"><span style="color:var(--teal);font-size:4px">&#10148;</span><p class="tx" style="font-size:3px;line-height:3.9px;color:var(--ink)">Short note on the first part of the problem here.</p></div>
    <div style="display:flex;gap:3px"><span style="color:var(--teal);font-size:4px">&#10148;</span><p class="tx" style="font-size:3px;line-height:3.9px;color:var(--ink)">Short note on the second part of the problem.</p></div>
    <div style="display:flex;gap:3px"><span style="color:var(--teal);font-size:4px">&#10148;</span><p class="tx" style="font-size:3px;line-height:3.9px;color:var(--ink)">Short note on the third part of the problem here.</p></div>
  </div>
  <div class="foot"><i class="foot-mark"></i><i class="pg">20</i></div>
</article>

<!-- 21 solution -->
<article class="slide">
  <svg class="abs" style="left:14px;top:12px" width="30" height="30" viewBox="0 0 30 30"><circle cx="15" cy="15" r="13" fill="none" stroke="var(--teal)" stroke-width="2.5"/><circle cx="15" cy="15" r="8" fill="#fff" stroke="var(--teal-l)" stroke-width=".8"/><path d="M11 15l3 3 5-6" fill="none" stroke="var(--teal)" stroke-width="1.4"/></svg>
  <h2 class="abs" style="left:62px;top:18px;font-size:8.5px;font-weight:700;color:var(--teal-d)">THE SOLUTION</h2>
  <p class="abs tx" style="left:62px;top:30px;width:120px;font-size:2.8px;line-height:3.6px">Short note on how our plan fixes the problem for each client.</p>
  <div class="abs" style="left:22px;top:52px;display:grid;grid-template-columns:100px 90px;gap:10px 14px">
    <div style="display:flex;gap:4px"><span style="width:8px;height:8px;border-radius:50%;background:var(--teal-xl);flex:none"></span><p class="tx" style="font-size:2.8px;line-height:3.6px">Short note on the first part of the fix and what it brings.</p></div>
    <div style="display:flex;gap:4px"><span style="width:8px;height:8px;border-radius:50%;background:var(--teal-xl);flex:none"></span><p class="tx" style="font-size:2.8px;line-height:3.6px">Short note on the second part of the fix and what it brings.</p></div>
    <div style="display:flex;gap:4px"><span style="width:8px;height:8px;border-radius:50%;background:var(--teal-xl);flex:none"></span><p class="tx" style="font-size:2.8px;line-height:3.6px">Short note on the third part of the fix and what it brings.</p></div>
    <div style="display:flex;gap:4px"><span style="width:8px;height:8px;border-radius:50%;background:var(--teal-xl);flex:none"></span><p class="tx" style="font-size:2.8px;line-height:3.6px">Short note on the fourth part of the fix and what it brings.</p></div>
  </div>
  <div class="foot"><i class="foot-mark"></i><i class="pg">21</i></div>
</article>

<!-- 22 value -->
<article class="slide">
  <div class="hdr"><span>Value</span></div>
  <svg class="abs" style="left:82px;top:24px" width="72" height="76" viewBox="0 0 72 76">
    <circle cx="44" cy="22" r="20" fill="var(--teal)"/>
    <circle cx="24" cy="44" r="20" fill="var(--teal-l)" opacity=".9"/>
    <circle cx="50" cy="52" r="20" fill="var(--teal-d)" opacity=".9"/>
    <g fill="#fff"><rect x="40" y="18" width="2" height="6"/><rect x="44" y="14" width="2" height="10"/><rect x="48" y="16" width="2" height="8"/><circle cx="22" cy="46" r="5"/><circle cx="52" cy="56" r="4" fill="none" stroke="#fff" stroke-width="1"/></g>
  </svg>
  <p class="abs tx" style="left:12px;top:38px;width:66px;font-size:2.9px;line-height:3.8px">Short note on the value we bring to each client and each guest at every event we run.</p>
  <p class="abs tx" style="left:12px;top:66px;width:66px;font-size:2.9px;line-height:3.8px">Short note on the time and money saved by one team with one plan.</p>
  <p class="abs tx" style="left:164px;top:56px;width:56px;font-size:2.9px;line-height:3.8px">Short note on the trust built with clients over many years.</p>
  <div class="foot"><i class="foot-mark"></i><i class="pg">22</i></div>
</article>

<!-- 23 hub -->
<article class="slide">
  <div class="hdr"><span>Lorem ipsum dolor sit</span></div>
  <svg class="abs" style="left:0;top:14px" width="229" height="105" viewBox="0 0 229 105" font-family="Open Sans, sans-serif" text-anchor="middle">
    <g stroke="var(--yel)" stroke-width="1"><path d="M115 52L84 28M115 52L84 52M115 52L98 82M115 52L150 22M115 52L150 50M115 52L132 82"/></g>
    <circle cx="115" cy="52" r="14" fill="var(--yel)"/>
    <text x="115" y="62" font-size="3" fill="#fff">Contents Title</text>
    <circle cx="84" cy="28" r="5" fill="#3dc6a7"/><circle cx="84" cy="52" r="5" fill="#ef8f3c"/><circle cx="98" cy="82" r="5" fill="var(--teal)"/>
    <circle cx="150" cy="22" r="5" fill="var(--slate)"/><circle cx="150" cy="50" r="5" fill="#ef8f3c"/><circle cx="132" cy="82" r="5" fill="var(--teal-l)"/>
    <rect x="34" y="18" width="34" height="5" rx="2.5" fill="var(--teal)"/><text x="51" y="21.6" font-size="2.8" fill="#fff">Contents Title</text>
    <rect x="24" y="80" width="34" height="5" rx="2.5" fill="var(--teal)"/><text x="41" y="83.6" font-size="2.8" fill="#fff">Contents Title</text>
    <rect x="170" y="10" width="34" height="5" rx="2.5" fill="var(--teal)"/><text x="187" y="13.6" font-size="2.8" fill="#fff">Contents Title</text>
    <rect x="170" y="46" width="34" height="5" rx="2.5" fill="var(--teal-l)"/><text x="187" y="49.6" font-size="2.8" fill="#fff">Contents Title</text>
  </svg>
  <p class="abs tx" style="left:34px;top:39px;width:40px;font-size:2.6px;line-height:3.3px">Short note on this part of the hub.</p>
  <p class="abs tx" style="left:24px;top:101px;width:44px;font-size:2.6px;line-height:3.3px">Short note on this part of the hub.</p>
  <p class="abs tx" style="left:170px;top:31px;width:44px;font-size:2.6px;line-height:3.3px">Short note on this part of the hub.</p>
  <p class="abs tx" style="left:170px;top:67px;width:44px;font-size:2.6px;line-height:3.3px">Short note on this part of the hub.</p>
  <div class="foot"><i class="foot-mark"></i><i class="pg">23</i></div>
</article>

<!-- 24 ring -->
<article class="slide">
  <div class="hdr"><span>Lorem ipsum dolor sit</span></div>
  <svg class="abs" style="left:82px;top:22px" width="66" height="94" viewBox="0 0 66 94" font-family="Open Sans, sans-serif" text-anchor="middle">
    <circle cx="33" cy="47" r="24" fill="none" stroke="#d5e6e7" stroke-width="1"/>
    <g fill="var(--teal-d)"><circle cx="33" cy="19" r="6"/><circle cx="53" cy="27" r="6"/><circle cx="61" cy="47" r="6"/><circle cx="53" cy="67" r="6"/><circle cx="33" cy="75" r="6"/><circle cx="13" cy="67" r="6"/><circle cx="5" cy="47" r="6"/><circle cx="13" cy="27" r="6"/></g>
    <circle cx="33" cy="47" r="14" fill="#fff" stroke="var(--teal-d)" stroke-width="1"/>
    <path d="M28 46l5-5 5 5v5h-10z" fill="var(--teal-d)"/>
    <text x="33" y="57" font-size="3.2" fill="var(--teal-d)">Text Here</text>
  </svg>
  <div class="abs" style="left:14px;top:22px;width:62px;display:grid;gap:5px;text-align:right">
    <div><div class="tt" style="font-size:3px;line-height:3.6px">Content Here</div><p class="tx" style="font-size:2.6px;line-height:3.3px">Short note for this item on the ring.</p></div>
    <div><div class="tt" style="font-size:3px;line-height:3.6px">Content Here</div><p class="tx" style="font-size:2.6px;line-height:3.3px">Short note for this item on the ring.</p></div>
    <div><div class="tt" style="font-size:3px;line-height:3.6px">Content Here</div><p class="tx" style="font-size:2.6px;line-height:3.3px">Short note for this item on the ring.</p></div>
    <div><div class="tt" style="font-size:3px;line-height:3.6px">Content Here</div><p class="tx" style="font-size:2.6px;line-height:3.3px">Short note for this item on the ring.</p></div>
  </div>
  <div class="abs" style="left:156px;top:22px;width:62px;display:grid;gap:5px">
    <div><div class="tt" style="font-size:3px;line-height:3.6px">Content Here</div><p class="tx" style="font-size:2.6px;line-height:3.3px">Short note for this item on the ring.</p></div>
    <div><div class="tt" style="font-size:3px;line-height:3.6px">Content Here</div><p class="tx" style="font-size:2.6px;line-height:3.3px">Short note for this item on the ring.</p></div>
    <div><div class="tt" style="font-size:3px;line-height:3.6px">Content Here</div><p class="tx" style="font-size:2.6px;line-height:3.3px">Short note for this item on the ring.</p></div>
    <div><div class="tt" style="font-size:3px;line-height:3.6px">Content Here</div><p class="tx" style="font-size:2.6px;line-height:3.3px">Short note for this item on the ring.</p></div>
  </div>
  <div class="foot"><i class="foot-mark"></i><i class="pg">24</i></div>
</article>
</section>

<section class="grid-last">
<!-- 25 data chart -->
<article class="slide">
  <div class="hdr"><span></span></div>
  <svg class="abs" style="left:14px;top:36px" width="100" height="80" viewBox="0 0 100 80" font-family="Open Sans, sans-serif" font-size="2.4" fill="#8c9295">
    <path d="M12 4v66h84" stroke="#d0d4d5" stroke-width=".4" fill="none"/>
    <g fill="var(--teal-l)"><rect x="18" y="56" width="6" height="14"/><rect x="30" y="50" width="6" height="20"/><rect x="42" y="32" width="6" height="38"/><rect x="54" y="14" width="6" height="56" fill="var(--teal)"/><rect x="66" y="26" width="6" height="44"/><rect x="78" y="44" width="6" height="26"/></g>
    <text x="21" y="76" text-anchor="middle">2010</text><text x="33" y="76" text-anchor="middle">2012</text><text x="45" y="76" text-anchor="middle">2014</text><text x="57" y="76" text-anchor="middle">2015</text><text x="69" y="76" text-anchor="middle">2017</text><text x="81" y="76" text-anchor="middle">2019</text>
  </svg>
  <h2 class="abs" style="left:124px;top:64px;font-size:9.5px;font-weight:600;color:var(--ink)">DATA CHART</h2>
  <p class="abs tx" style="left:124px;top:78px;width:88px;font-size:2.8px;line-height:3.6px">Short note that reads the chart and points out the best year for us.</p>
  <div class="foot"><i class="foot-mark"></i><i class="pg">25</i></div>
</article>

<!-- 26 get in touch -->
<article class="slide">
  <h2 class="abs" style="left:42px;top:41px;font-size:9px;font-weight:600;color:var(--teal)">Get in Touch</h2>
  <p class="abs tx" style="left:42px;top:54px;width:78px;text-align:center;font-size:2.9px;line-height:3.8px">Short note inviting readers to call or write to us. We reply within a day and help plan the next event with you.</p>
  <svg class="abs" style="left:160px;top:8px" width="50" height="108" viewBox="0 0 50 108" font-family="Open Sans, sans-serif" font-size="2.6" fill="var(--ink)" text-anchor="middle">
    <circle cx="25" cy="8" r="4" fill="none" stroke="var(--teal-d)" stroke-width=".8"/><path d="M21 8h8M25 4v8" stroke="var(--teal-d)" stroke-width=".6"/>
    <text x="25" y="18">www.YOURWEBSITE.com</text>
    <path d="M22 32l2-2 2 2-1 1 3 3 1-1 2 2-2 2c-4 0-8-4-8-8z" fill="var(--teal-d)"/>
    <text x="25" y="44">555.555.5555</text>
    <rect x="20" y="58" width="10" height="7" fill="var(--teal-d)"/><path d="M20 58l5 4 5-4" fill="none" stroke="#fff" stroke-width=".6"/>
    <text x="25" y="72">info@YOURSITE.com</text>
    <path d="M25 96c-3-4-4-6-4-8a4 4 0 0 1 8 0c0 2-1 4-4 8z" fill="var(--teal-d)"/>
    <text x="25" y="102">Your company adress</text>
  </svg>
  <div class="foot"><i class="foot-mark"></i><i class="pg">26</i></div>
</article>
</section>
</main>
</body>
</html>
```